The Velmira Circle

I need a design for a 1 page flyer but also a brochure

Target Market(s)

Wealthy, elegant, intelligent, discerning women who are on a journey of self-discovery.

Industry/Entity Type

Spiritual and personal development, yoga, meditation

Requirements
Must have
• Be very elegant, attractive, upmarket minimalist but also bit mystical
Nice to have
• I would like to use my logo (see uploaded file). The texts are also uploaded. One for the 1 page flyer 1 for a full brochure
Should not have
• be too busy, multicoloured, garish.

```html
<!DOCTYPE html>
<html lang="en">
<head>
<meta charset="utf-8">
<title>The Velmira Circle – Pathways to Our True Essence</title>
<link href="https://fonts.googleapis.com/css2?family=Cinzel:wght@400;600;700&family=Montserrat:wght@300;400;500&display=swap" rel="stylesheet">
<style>
  :root{
    --stage:#a8a8a8;
    --forest:#1f5a2a;
    --forest-deep:#123d1b;
    --forest-mid:#24672f;
    --cream:#f5f0e2;
    --paper:#ffffff;
    --sage:#eef3e3;
    --ink:#2b2b2b;
    --grey-type:#7d7d78;
    --rule:#b9b6aa;
    --photo-sky:#8fb3b9;
    --photo-grass:#6f9a45;
  }
  *{box-sizing:border-box;margin:0;padding:0}
  html,body{width:799px;height:1200px;overflow:hidden;background:var(--stage)}
  body{position:relative;font-family:'Montserrat',sans-serif;color:var(--ink)}
  .spread{position:absolute;left:20px;width:760px;height:294px;box-shadow:0 6px 14px rgba(0,0,0,.25);overflow:hidden}
  .spread--outside{top:291px}
  .spread--inside{top:615px}
  .abs{position:absolute}

  /* panels */
  .panel-cream{left:0;top:0;width:287px;height:294px;background:var(--cream)}
  .panel-green{top:0;height:294px;background:radial-gradient(ellipse at 60% 40%,var(--forest-mid),var(--forest-deep) 95%)}
  .panel-white{top:0;height:294px;background:var(--paper)}

  .v-rule{width:.6px;background:var(--rule)}
  .v-rule--light{background:rgba(255,255,255,.35)}

  /* photo placeholders */
  .photo{background:linear-gradient(170deg,var(--photo-sky) 0%,#b9c7b3 45%,var(--photo-grass) 100%)}
  .photo--framed{outline:3px solid #fff;outline-offset:-3px}
  .photo--studio{background:linear-gradient(180deg,#d8cbb8,#9a8d7e)}
  .photo--meadow{background:linear-gradient(180deg,#a9c6d8,#c9b94a 60%,#6d8f35)}
  .photo--lake{background:linear-gradient(180deg,#c7d2d8,#7fa0b3 55%,#b49a5a)}

  /* outside: quote panel */
  .quote-mark{left:47px;top:28px;font-family:'Cinzel',serif;font-size:22px;color:var(--forest);line-height:1}
  .quote{left:49px;top:49px;font-family:'Cinzel',serif;font-weight:700;font-size:12.4px;line-height:15px;color:var(--forest)}
  .quote .muted{color:var(--grey-type)}
  .quote .close{font-weight:400;font-size:18px;color:var(--forest);vertical-align:-4px}
  .h-rule{left:51px;top:141px;width:82px;height:.6px;background:var(--rule)}
  .brand-small{left:47px;top:203px;font-family:'Montserrat',sans-serif;font-weight:300;font-size:7.5px;letter-spacing:.5px;line-height:9px;color:var(--forest);display:flex;align-items:center;gap:5px}
  .brand-small .dot{width:9px;height:9px;border-radius:50%;background:var(--forest)}
  .contacts{left:46px;top:235px;font-size:8.4px;line-height:11.2px;color:var(--ink);list-style:none}
  .contacts li{display:flex;align-items:center;gap:4px}
  .contacts svg{width:7px;height:7px}

  /* outside: cover */
  .brand-cover{left:371px;top:62px;width:120px;text-align:center;font-weight:300;font-size:9.6px;letter-spacing:.6px;line-height:12px;color:rgba(255,255,255,.75)}
  .brand-cover .dot{display:block;width:18px;height:18px;border-radius:50%;background:#fff;margin:0 auto 8px}
  .cover-kicker{left:402px;top:140px;font-family:'Cinzel',serif;font-size:16.5px;color:#fff;letter-spacing:.3px}
  .cover-title{left:401px;top:158px;font-family:'Cinzel',serif;font-weight:700;font-size:35px;line-height:33px;color:#fff}
  .cover-place{left:402px;top:245px;font-family:'Cinzel',serif;font-weight:700;font-size:11px;color:#fff;letter-spacing:.3px}
  .cover-date{left:402px;top:259px;font-family:'Cinzel',serif;font-size:7px;color:rgba(255,255,255,.8);letter-spacing:1px}
  .corner-frame{left:660px;top:214px;width:78px;height:56px;border-right:.7px solid rgba(255,255,255,.55);border-bottom:.7px solid rgba(255,255,255,.55)}

  /* inside */
  .section-title{font-family:'Cinzel',serif;font-weight:700;font-size:6.6px;letter-spacing:.2px}
  .on-dark{color:#fff}
  .on-light{color:var(--forest)}
  .body-copy{font-size:4.3px;line-height:5.75px;text-align:justify}
  .body-copy.on-dark{color:rgba(255,255,255,.9)}
  .body-copy.on-light{color:#333}
  .hold-box{left:223px;top:50px;width:135px;height:127px;background:var(--sage);padding:18px 17px 0 17px}
  .hold-box .section-title{font-size:7px;margin-bottom:5px}
  .page-no{font-family:'Cinzel',serif;font-size:4.2px;color:#666}
  .page-no.on-dark{color:rgba(255,255,255,.75)}
  .pathways{left:414px;top:144px;list-style:none}
  .pathways li{width:89px;height:10.5px;margin-bottom:4.3px;border:.5px solid #c9c9c2;border-radius:6px;font-size:4.3px;display:flex;align-items:center;padding-left:4px;gap:3px;color:#333}
  .pathways li::before{content:"";width:3px;height:3px;border-radius:50%;background:var(--forest)}
  .about-title{left:624px;top:46px;font-family:'Cinzel',serif;color:#fff;line-height:1}
  .about-title .small{font-size:17px;display:block}
  .about-title .big{font-size:28px;font-weight:600;display:block;margin:-6px 0 0 56px}
</style>
</head>
<body>

<!-- Outside spread -->
<section class="spread spread--outside">
  <div class="abs panel-cream"></div>
  <div class="abs v-rule" style="left:29px;top:44px;height:220px"></div>
  <div class="abs quote-mark">“</div>
  <p class="abs quote">WITHIN THE<br>QUIET OF YOUR<br>BEING, YOUR<br><span class="muted">ESSENCE WAITS TO<br>BE REMEMBERED</span> <span class="close">”</span></p>
  <div class="abs h-rule"></div>
  <div class="abs brand-small"><span class="dot"></span><span>THE VELMIRA<br>CIRCLE</span></div>
  <ul class="abs contacts">
    <li><svg viewBox="0 0 10 10"><circle cx="5" cy="5" r="5" fill="#1f5a2a"/><path d="M3.3 2.8l1 1-.5.6a3 3 0 001.8 1.8l.6-.5 1 1-.6.7c-2 0-3.9-1.9-3.9-3.9z" fill="#fff"/></svg>+41 79 000 48 20</li>
    <li><svg viewBox="0 0 10 10"><circle cx="5" cy="5" r="5" fill="#1f5a2a"/><rect x="2.6" y="3.3" width="4.8" height="3.4" fill="none" stroke="#fff" stroke-width=".7"/><path d="M2.6 3.3L5 5.2l2.4-1.9" fill="none" stroke="#fff" stroke-width=".7"/></svg>hello@velmira-circle.com</li>
    <li><svg viewBox="0 0 10 10"><circle cx="5" cy="5" r="5" fill="#1f5a2a"/><circle cx="5" cy="5" r="2.4" fill="none" stroke="#fff" stroke-width=".7"/><path d="M2.6 5h4.8" stroke="#fff" stroke-width=".6"/></svg>www.velmira-circle.com</li>
  </ul>
  <div class="abs photo photo--studio" style="left:253px;top:73px;width:67px;height:83px" role="img" aria-label="Woman meditating cross-legged in a bright studio"></div>
  <div class="abs photo photo--lake photo--framed" style="left:287px;top:157px;width:71px;height:89px" role="img" aria-label="Woman kneeling in prayer pose by a lake at sunrise"></div>
  <div class="abs photo photo--meadow" style="left:215px;top:181px;width:67px;height:83px" role="img" aria-label="Smiling woman in a field of yellow flowers"></div>

  <div class="abs panel-green" style="left:287px;width:473px"></div>
  <div class="abs brand-cover"><span class="dot"></span>THE VELMIRA<br>CIRCLE</div>
  <p class="abs cover-kicker">PATHWAYS TO OUR</p>
  <h1 class="abs cover-title">TRUE<br>ESSENCE</h1>
  <p class="abs cover-place">TUSCANY, ITALY</p>
  <p class="abs cover-date">25–29 JUNE 2026</p>
  <div class="abs corner-frame"></div>
  <div class="abs photo" style="left:595px;top:74px;width:136px;height:189px" role="img" aria-label="Woman meditating on a green hillside above misty valleys"></div>
</section>

<!-- Inside spread -->
<section class="spread spread--inside">
  <div class="abs panel-green" style="left:0;width:279px"></div>
  <div class="abs v-rule v-rule--light" style="left:29px;top:44px;height:220px"></div>
  <h2 class="abs section-title on-dark" style="left:43px;top:50px">WHY I CREATED THIS RETREAT</h2>
  <p class="abs body-copy on-dark" style="left:43px;top:65px;width:158px">My path with yoga began many years ago, during a demanding career that kept me moving between cities. At first my body felt stiff and restless, and I could not understand what the practice was asking of me. Slowly, on the mat, I began to notice small moments of awareness that I had never experienced before: the soles of my feet, the palms of my hands, a softening along my spine. Later, as I left a fast, travel-heavy life, I trained for long-distance running and used yoga only as stretching. Yet the stillness kept calling. One quiet morning I realised that an hour of breath and movement had calmed my mind more deeply than any race. Yoga was not simply physical; it was one doorway inward. I stepped into my first teacher training to understand, not to teach, and it felt like entering a new world. Through years of practice, curiosity, study and exploration I have come to understand something essential: there is no single path. Each of us is unique, and each of us will resonate with different tools at different moments. What supports us today may shift tomorrow. This retreat is rooted in that philosophy. It is a discerning, intelligent and elegant container for gentle yet deep inner work. My intention is to offer a constellation of practices, so that you may discover what truly serves you. The group remains intentionally small so that each person receives attention, guidance and care. This is an invitation to step toward your essence, in your own way, at your own rhythm.</p>

  <div class="abs panel-white" style="left:279px;width:321px"></div>
  <div class="abs hold-box">
    <h3 class="section-title on-light">HOW I HOLD SPACE</h3>
    <p class="body-copy on-light">I have cultivated a quiet, practised intuition that allows me to meet people exactly where they are. Through energy work, meditation and somatics I have learned to sense subtle shifts within a room or within one person. This attunement shows me when to guide, when to soften, and when to simply allow, and when needed, when to be clear and firm. I hold space gently, so that no one slips away from the very work they came to meet.</p>
  </div>
  <div class="abs photo" style="left:223px;top:180px;width:66px;height:70px" role="img" aria-label="Man meditating cross-legged outdoors before mountains"></div>
  <div class="abs photo" style="left:292px;top:180px;width:66px;height:70px" role="img" aria-label="Woman meditating on a mat in a green garden"></div>
  <p class="abs page-no" style="left:344px;top:263px">PAGE 1</p>

  <div class="abs v-rule" style="left:401px;top:44px;height:220px"></div>
  <h2 class="abs section-title on-light" style="left:416px;top:50px">WHY I CREATED THIS RETREAT</h2>
  <p class="abs body-copy on-light" style="left:416px;top:65px;width:167px">My approach rests on the understanding that self-discovery is never linear or prescriptive. We each arrive with different histories, patterns and sensitivities, so no single method speaks to everyone in the same way. I offer a curated selection of practices, movement, breath, somatics, meditation and energy work, so that you can feel what truly resonates. I invite you to explore with curiosity rather than expectation, leaving room for insight, release or stillness to arise naturally, always honouring your autonomy and inner wisdom.</p>
  <h2 class="abs section-title on-light" style="left:416px;top:132px">PATHWAYS WE WILL EXPLORE</h2>
  <ul class="abs pathways">
    <li>Evolve Your Energy</li>
    <li>Immerse in Frequency</li>
    <li>Harness Your Breath</li>
    <li>Embodied Awakening</li>
    <li>Shadow Exploration</li>
    <li>Reiki Healing</li>
    <li>Forest Bathing</li>
    <li>Centering at Your Fingertips</li>
  </ul>

  <div class="abs panel-green" style="left:600px;width:160px"></div>
  <h2 class="abs about-title"><span class="small">ABOUT</span><span class="big">ME</span></h2>
  <p class="abs body-copy on-dark" style="left:624px;top:96px;width:108px">I am an Ashtanga practitioner who teaches many styles of yoga, dynamic, hatha, yin and nidra, with a somatic and intuitive approach. I teach meditation, breathwork and energy practices, and I am a certified senior teacher with advanced training in pranayama and meditation. I am also a certified coach. My earlier career spanned international development with global institutions and inclusive organisations, and later my own consultancy on human potential. These experiences shaped my ability to listen deeply, hold space and support change with clarity and compassion.</p>
  <h3 class="abs section-title on-dark" style="left:624px;top:206px;line-height:7.5px">A JOURNEY THROUGH<br>THE INNER REALMS</h3>
  <p class="abs body-copy on-dark" style="left:624px;top:225px;width:108px">As these pathways weave together, a deeper journey unfolds, a movement from the surface of daily life into the quiet, spacious layers of the inner world.</p>
  <p class="abs page-no on-dark" style="left:716px;top:263px">PAGE 2</p>
</section>

</body>
</html>
```